Driving School needs brochure for clients charged before the courts with Road Rage

We are a driving school who provides courses to those charged with driving with road rage. This brochure which will be a pdf trifold will be emailed to lawyers, judges and clients. Needs to be extremely professional modern and classy.

Target Market(s)

judges, lawyers

Font styles to use
Serif
Sans Serif

Requirements
Must have
• Please replicate the current Savor the Trip brochure regarding the front page and graphic.
Final design will be a single pdf document with front page of trifold at top and inner at bottom. Should look similar in deign to Caution Mindful (brown brochure) brochure. Not same color. Final panel should be very similar/identical and same as middle panel on outside of trifold (top middle panel) i.e., contact information with phone number, email and website should be similar/identical.
Should not have
• any manufacturer name/logo or image that is obviously linked

```html
<!DOCTYPE html>
<html lang="en">
<head>
<meta charset="utf-8">
<title>Caution Mindful – Trifold Brochure</title>
<link href="https://fonts.googleapis.com/css2?family=Oswald:wght@300;400;500;600&family=Open+Sans:ital,wght@0,400;0,600;0,700;1,600;1,700&family=Montserrat:ital,wght@1,500&family=Tinos:ital,wght@0,400;1,400&display=swap" rel="stylesheet">
<style>
:root{
  --page:#e8e9ec;
  --navy:#2a4a85;
  --navy-mid:#2f5194;
  --navy-dark:#203a6b;
  --sky:#6fa6d6;
  --accent-blue:#4fb0e3;
  --cost:#e2542a;
  --white:#ffffff;
  --ink:#1f2e4f;
}
*{box-sizing:border-box;margin:0;padding:0}
html,body{width:1200px;height:4624px;overflow:hidden;background:var(--page)}
body{font-family:"Open Sans",Arial,sans-serif;color:var(--ink);position:relative}
.spread{position:absolute;left:60px;width:1080px;height:836px;box-shadow:0 6px 18px rgba(0,0,0,.18);overflow:hidden}
.spread--outside{top:1420px;background:var(--navy)}
.spread--inside{top:2356px;background:var(--white)}
.panel{position:absolute;top:0;width:360px;height:836px}
.panel--left{left:0}.panel--middle{left:360px}.panel--right{left:720px}
.abs{position:absolute}
.cond{font-family:"Oswald",sans-serif}
.serif{font-family:"Tinos",serif}

/* outside: background panel */
.bg-heading{position:absolute;left:0;top:26px;width:190px;padding:4px 0 4px 22px;background:var(--navy-dark);border-bottom:2px solid var(--white);font-family:"Oswald",sans-serif;font-weight:500;font-size:21px;color:var(--white)}
.bg-copy{position:absolute;left:22px;top:78px;width:318px;color:var(--white);font-size:9.6px;line-height:13.4px;text-align:justify}
.bg-copy p{margin-bottom:13px}
.photo{position:absolute}
.photo--drink{left:22px;top:592px;width:316px;height:222px;background:linear-gradient(135deg,#5a3b24 0%,#a86b32 45%,#3f2c1f 100%)}

/* outside: contact panel */
.contact-panel{background:var(--navy-mid)}
.tagline{position:absolute;left:0;top:84px;width:360px;text-align:center;font-family:"Montserrat",sans-serif;font-style:italic;font-weight:500;font-size:25px;line-height:56px;color:var(--white)}
.info-label{position:absolute;left:0;top:548px;width:360px;text-align:center;font-family:"Oswald",sans-serif;font-size:15px;letter-spacing:4px;color:var(--white)}
.phone-big{position:absolute;left:0;top:578px;width:360px;text-align:center;font-family:"Oswald",sans-serif;font-size:40px;color:var(--white);display:flex;justify-content:center;align-items:center;gap:8px}
.pill{position:absolute;border-radius:20px;text-align:center;font-weight:700;font-size:9.6px;line-height:13px;padding:5px 0}
.pill--light{left:32px;top:648px;width:296px;background:var(--white);color:var(--navy)}
.road-corner{position:absolute;left:0;bottom:0;width:170px;height:120px;background:radial-gradient(circle at 0 100%,#1b2f57 0%,#36558f 70%,transparent 71%)}

/* outside: cover */
.cover{background:var(--white)}
.cover-photo{position:absolute;left:0;top:0;width:360px;height:520px;background:linear-gradient(180deg,#d9e8f5 0%,#7fb2dc 22%,#c9cfd6 40%,#6b6e73 58%,#2e3034 100%)}
.cover-title{position:absolute;left:0;top:14px;width:360px;text-align:center;font-family:"Oswald",sans-serif;font-weight:500;font-size:50px;color:var(--navy);letter-spacing:.5px}
.cover-sub{position:absolute;left:0;top:394px;width:360px;text-align:center;font-family:"Oswald",sans-serif;font-weight:300;font-size:26px;line-height:30px;color:var(--white)}
.cover-sub b{font-weight:500}
.school-name{position:absolute;left:0;top:536px;width:360px;text-align:center;font-family:"Oswald",sans-serif;font-weight:600;font-size:24px;color:var(--navy)}
.school-line{position:absolute;left:0;top:574px;width:360px;text-align:center;font-size:11px;font-weight:600;color:var(--navy)}
.serif-note{position:absolute;left:0;width:360px;text-align:center;font-family:"Tinos",serif;font-size:13px;line-height:16px;color:var(--ink)}
.serif-note b{color:var(--navy)}
.phone-navy{position:absolute;left:0;top:680px;width:360px;text-align:center;font-family:"Oswald",sans-serif;font-weight:500;font-size:46px;color:var(--navy)}
.pill--navy{left:44px;top:758px;width:272px;background:var(--navy);color:var(--white);font-weight:600}

/* inside */
.wave{position:absolute}
.in-title{position:absolute;left:22px;top:74px;font-family:"Oswald",sans-serif;font-weight:500;font-size:22px;color:var(--navy)}
.in-intro{position:absolute;left:22px;top:110px;width:310px;font-style:italic;font-weight:700;font-size:10px;line-height:13px;color:var(--ink)}
.in-intro p{margin-bottom:10px}
.tab{position:absolute;left:0;top:206px;width:232px;padding:3px 0 3px 22px;background:var(--navy);font-family:"Oswald",sans-serif;font-weight:500;font-size:21px;color:var(--white)}
.topics{position:absolute;left:22px;width:310px;font-size:9.6px;line-height:12.6px;color:var(--ink)}
.topics h4{font-size:12.5px;font-weight:700;color:var(--navy);margin:10px 0 4px}
.topics h4:first-child{margin-top:0}
.topics ul{list-style:none}
.topics li{padding-left:9px;position:relative;margin-bottom:3px}
.topics li::before{content:"•";position:absolute;left:0}
.pill--url{left:22px;top:790px;width:300px;background:var(--navy);color:var(--white);letter-spacing:1.5px;font-size:10px}
.tailored{position:absolute;left:0;top:700px;width:360px;text-align:center;font-family:"Oswald",sans-serif;font-weight:500;font-size:30px;line-height:31px;color:var(--white)}
.tailored span{color:var(--accent-blue)}
.remote-title{position:absolute;left:0;top:36px;width:360px;text-align:center;font-family:"Oswald",sans-serif;font-weight:500;font-size:48px;line-height:52px;color:var(--navy)}
.remote-illus{position:absolute;left:40px;top:170px;width:290px;height:230px;border-radius:6px;background:linear-gradient(135deg,#e8f0fa 0%,#b9d3ee 55%,#f2c98a 100%)}
.cost{position:absolute;left:72px;top:446px;width:216px;height:216px;border-radius:50%;background:var(--white);border:6px solid var(--navy);text-align:center;padding-top:42px}
.cost-label{font-family:"Oswald",sans-serif;font-size:20px;color:var(--navy)}
.cost-amount{font-family:"Oswald",sans-serif;font-weight:500;font-size:50px;line-height:52px;color:var(--cost)}
.serif-note--light{color:var(--white)}
.serif-note--light b{color:var(--white)}
.pill--white{left:44px;top:782px;width:272px;background:var(--white);color:var(--navy);font-weight:600}
</style>
</head>
<body>

<!-- OUTSIDE SPREAD -->
<section class="spread spread--outside" aria-label="Brochure outside">
  <div class="panel panel--left">
    <h2 class="bg-heading">OUR BACKGROUND:</h2>
    <div class="bg-copy">
      <p>Since its inception in 1998, Lane Sense Driving School has strived to help drivers maintain their driving independence while leading safe and productive lives. Our motto “making drivers safe for life” drives our vision of helping drivers across industries and at all stages of our driving careers.</p>
      <p>Lane Sense started out working with school boards to deliver driver training to beginner drivers. Thousands of students have graduated from our ministry-approved curriculum. We are also ministry-approved to instruct defensive driving (DDC) and driver improvement courses (DIC), for drivers with speeding tickets, demerit points and at fault crashes.</p>
      <p>Lane Sense has also evolved to provide comprehensive driver rehabilitation to those who have lost, or are at risk of losing their license for medical reasons. This includes mobility issues requiring adaptive equipment, as well as traumatic crashes resulting in cognitive impairments and PTSD. We work with clients before the courts charged with impaired driving (alcohol, cannabis, opioids), road rage and stunt driving.</p>
      <p>Founder Michael Hale started driving at an early age on his parent’s farm. Driving professionally and doing so safely is in his DNA. Michael has a degree in Business and Psychology and is a certified in-car and in-class driving instructor.</p>
    </div>
    <div class="photo photo--drink" role="img" aria-label="Photo of a glass of whisky beside car keys and handcuffs on a wooden table"></div>
  </div>

  <div class="panel panel--middle contact-panel">
    <p class="tagline">Maintaining<br>driving independence,<br>while leading<br>safe and<br>productive<br>lives!</p>
    <p class="info-label">FOR MORE INFORMATION</p>
    <p class="phone-big">
      <svg width="26" height="26" viewBox="0 0 24 24" aria-hidden="true"><path fill="#fff" d="M6.6 10.8a15.1 15.1 0 0 0 6.6 6.6l2.2-2.2c.3-.3.7-.4 1-.2 1.1.4 2.3.6 3.6.6.6 0 1 .4 1 1V20c0 .6-.4 1-1 1A17 17 0 0 1 3 4c0-.6.4-1 1-1h3.5c.6 0 1 .4 1 1 0 1.3.2 2.5.6 3.6.1.3 0 .7-.2 1z"/></svg>
      555-310-4827
    </p>
    <p class="pill pill--light">www.lanesensedriving.ca<br>mhale@lanesensedriving.ca</p>
    <div class="road-corner" role="img" aria-label="Corner photo of a curving road"></div>
  </div>

  <div class="panel panel--right cover">
    <div class="cover-photo" role="img" aria-label="Photo of a straight desert highway with yellow centre lines under a blue sky"></div>
    <h1 class="cover-title">CAUTION MINDFUL</h1>
    <p class="cover-sub">A 1-DAY EDUCATIONAL COURSE<br>FOR THOSE CHARGED WITH<br><b>DRINKING AND DRIVING</b></p>
    <p class="school-name">Lane Sense Driving School</p>
    <p class="school-line">Making drivers safe...for life!</p>
    <p class="serif-note" style="top:630px">For all your <b>G License</b> needs!<br><i>Beginner, Rehabilitation &amp; Remedial</i></p>
    <p class="phone-navy">555-310-4827</p>
    <p class="pill pill--navy">www.lanesensedriving.ca<br>mhale@lanesensedriving.ca</p>
  </div>
</section>

<!-- INSIDE SPREAD -->
<section class="spread spread--inside" aria-label="Brochure inside">
  <svg class="wave" style="left:0;top:0" width="720" height="90" viewBox="0 0 720 90" aria-hidden="true">
    <path fill="var(--navy)" d="M0 0H720V8C560 8 500 58 330 58C200 58 90 40 0 62Z"/>
  </svg>
  <svg class="wave" style="left:360px;top:600px" width="720" height="236" viewBox="0 0 720 236" aria-hidden="true">
    <path fill="var(--navy)" d="M0 236V150C80 80 220 70 360 96V236Z"/>
    <path fill="var(--navy)" d="M360 96C430 110 480 60 560 44C640 28 690 60 720 56V236H360Z"/>
  </svg>

  <div class="panel panel--left">
    <h2 class="in-title">CAUTION MINDFUL:</h2>
    <div class="in-intro">
      <p>A 1-day, 7-hour, intensive remedial measures course for those charged with driving under the influence of alcohol.</p>
      <p>Our goal is to equip our customers with knowledge and to help them avoid something devastating and/or irreversible from happening in the future.</p>
    </div>
    <h3 class="tab">TOPICS COVERED:</h3>
    <div class="topics" style="top:252px">
      <h4>Law:</h4>
      <ul><li>Highway Traffic Act (privilege vs right)</li><li>Federal and Provincial</li><li>Implications of criminal record (financial, work, relationships, etc.)</li></ul>
      <h4>Road Rage:</h4>
      <ul><li>Triggers</li><li>Personality types (Type A); Holmes &amp; Rahe stress scale</li><li>Aggressive driving (overlap between aggressors and victims)</li><li>Psychiatric issues/PTSD: Not uncommon to have professional drivers come through the course due to over-exposure to stress from driving (both on the job or the commute to their driving job)</li></ul>
      <h4>Physiology and the negative impacts of stress on the body</h4>
      <ul><li>Fight or flight response: how it works</li><li>Hormones (Adrenaline, Cortisol, etc.)</li><li>Chronic levels of exposure/Immune system suppression, hypertension</li><li>Substances (will do brief overview of drinking and driving if relevant i.e., individual risk factors and thresholds)</li></ul>
    </div>
    <p class="pill pill--url">www.lanesensedriving.ca</p>
  </div>

  <div class="panel panel--middle">
    <div class="topics" style="top:104px">
      <h4>Strategies to manage:</h4>
      <ul><li>Window of tolerance (hyper-arousal vs hypo-arousal)</li><li>Breathing: how to have the cerebral part of the brain making decisions and not “lizard” part of brain</li><li>We look at how our bodies have not kept up from an evolutionary point of view to manage daily stresses and stimuli</li><li>Our habits: approx. 50% of our decisions are made with little to no decision-making process; stages of change theory</li></ul>
      <h4>Personal context:</h4>
      <ul><li>Genetics &amp; socialization (role models &amp; predispositions)</li><li>Analysis of triggers leading up to event; what is really causing it, e.g., sometimes it can be systemic such as our commute</li></ul>
      <h4>Defensive Driving skills:</h4>
      <ul><li>The golden rule: Following distance</li><li>Defensive stopping (what we should do every time we apply brakes)</li><li>Using your eyes and strategic driving</li><li>Driving in adverse conditions-they exist every time we drive (human, environmental, machine)</li></ul>
    </div>
    <p class="tailored">COURSES ARE<br>INDIVIDUALLY TAILORED<br><span>ONE-ON-ONE.</span></p>
  </div>

  <div class="panel panel--right">
    <h2 class="remote-title">OFFERED<br>REMOTELY!</h2>
    <div class="remote-illus" role="img" aria-label="Illustration of an instructor presenting an online course with floating app icons"></div>
    <div class="cost">
      <p class="cost-label">COURSE COST:</p>
      <p class="cost-amount">$775.00<br>+ HST</p>
    </div>
    <p class="serif-note serif-note--light" style="top:740px">For all your <b>G License</b> needs!<br><i>Beginner, Rehabilitation &amp; Remedial</i></p>
    <p class="pill pill--white">www.lanesensedriving.ca<br>mhale@lanesensedriving.ca</p>
  </div>
</section>

</body>
</html>
```